New Interrior Decoration company needs new website

We need a website for our new company specialising in interior decoration to residential and commercial markets.
We supply and install decorative and printed films for office and home decoration such as feature walls.
We would like to keep the design simple and clean.

Target Market(s)

Architects and interior designaers

Industry/Entity Type

It Company

Number of Pages Required

5+ page

Font styles to use
Sans Serif

Requirements
Must have
• Home page,
• Services/products page (split into commercial and residential)
• Gallery (split into commercial and residential)
• contact form and page
Nice to have
• Very clean and minimalistic design.

```html
<!DOCTYPE html>
<html lang="en">
<head>
<meta charset="utf-8">
<title>Vantage Interiors</title>
<link href="https://fonts.googleapis.com/css2?family=Montserrat:wght@300;400;500;600;700&family=Open+Sans:wght@400;600&display=swap" rel="stylesheet">
<style>
:root{
  --blue:#2a69b3;
  --blue-deep:#24609f;
  --ink:#141414;
  --text:#666;
  --muted:#8a8a8a;
  --line:#e2e2e2;
  --white:#fff;
  --footer:#2a6cb8;
}
*{margin:0;padding:0;box-sizing:border-box}
html,body{width:1200px;height:2773px;overflow:hidden;background:var(--white)}
body{position:relative;font-family:"Open Sans",Arial,sans-serif;color:var(--text)}
.abs{position:absolute}
.center{left:0;width:1200px;text-align:center}

/* header */
.site-header{position:absolute;left:0;top:0;width:1200px;height:120px;background:var(--white)}
.brand{position:absolute;left:100px;top:30px;display:flex;align-items:center;gap:10px}
.brand-mark{width:52px;height:52px;background:var(--blue)}
.brand-name{font-family:"Montserrat",sans-serif;font-weight:700;font-size:27px;line-height:26px;color:#1f2a3a;letter-spacing:-.5px}
.main-nav a{position:absolute;top:57px;font-family:"Montserrat",sans-serif;font-weight:600;font-size:13.5px;color:var(--ink);text-decoration:none;letter-spacing:.3px}
.main-nav a.active{color:var(--blue)}
.nav-underline{position:absolute;left:527px;top:116px;width:66px;height:4px;background:var(--blue)}

/* hero */
.hero{position:absolute;left:0;top:120px;width:1200px;height:601px;background:linear-gradient(160deg,#5c6470 0%,#7b8591 35%,#9aa3ad 60%,#5a5f66 100%)}
.hero-title{position:absolute;top:222px;left:0;width:1200px;text-align:center;font-family:"Montserrat",sans-serif;font-weight:700;font-size:54px;color:var(--white);letter-spacing:1px}
.hero-curve{position:absolute;left:0;top:0}
.dots{position:absolute;display:flex;gap:5px}
.dot{width:15px;height:15px;border-radius:50%;background:var(--white)}
.dot.hollow{background:transparent;border:2px solid var(--white)}

/* welcome */
.section-title{font-family:"Montserrat",sans-serif;font-weight:700;font-size:31px;color:var(--ink);letter-spacing:.5px}
.section-title .accent{color:var(--blue)}
.lead{font-size:13px;line-height:23px;color:var(--muted)}
.market-card{position:absolute;top:913px;width:370px;height:170px;background:var(--white);border:1px solid #ededed;box-shadow:0 14px 12px -10px rgba(0,0,0,.18)}
.market-card h3{position:absolute;left:97px;top:34px;font-family:"Montserrat",sans-serif;font-weight:500;font-size:18px;color:var(--blue);letter-spacing:.5px}
.market-card p{position:absolute;left:97px;top:72px;width:250px;font-size:11.5px;line-height:21px;color:var(--muted)}
.market-card svg{position:absolute;left:14px;top:70px}

/* specialise band */
.specialise{position:absolute;left:0;top:1146px;width:1200px;height:455px;background:linear-gradient(180deg,#2e63a5 0%,#3a72b6 55%,#5a8fcc 80%,#2f65a8 100%)}
.specialise h2{position:absolute;top:68px;left:0;width:1200px;text-align:center;font-family:"Montserrat",sans-serif;font-weight:300;font-size:44px;line-height:43px;color:var(--white)}
.specialise p{position:absolute;top:178px;left:170px;width:860px;text-align:center;font-size:13.5px;line-height:26px;color:#e6eef8}
.btn-outline{position:absolute;left:490px;top:292px;width:218px;height:50px;border:1.5px solid rgba(255,255,255,.85);color:var(--white);font-family:"Montserrat",sans-serif;font-weight:500;font-size:19px;letter-spacing:1px;text-align:center;line-height:47px}

/* services */
.service-card{position:absolute;top:1769px;width:312px;height:252px;border:1px solid var(--line);background:var(--white)}
.service-photo{position:absolute;left:25px;top:20px;width:261px;height:181px}
.service-card h3{position:absolute;left:0;top:214px;width:100%;text-align:center;font-family:"Montserrat",sans-serif;font-weight:400;font-size:19px;color:#333}

/* testimonial */
.testimonials{position:absolute;left:0;top:2086px;width:1200px;height:366px;background:linear-gradient(180deg,#e7dfe3 0%,#e4e1e6 45%,#dcdee4 75%,#e6e4e8 100%)}
.quote-mark{position:absolute;font-family:Georgia,serif;font-size:70px;color:#b9b6ba;line-height:1}
.quote-text{position:absolute;left:188px;top:120px;width:824px;text-align:center;font-size:11.5px;line-height:22px;color:#444}
.quote-author{position:absolute;top:221px;left:0;width:1200px;text-align:center;font-size:12.5px;color:var(--ink)}
.quote-author .name{color:var(--blue)}
.dot.grey{background:#6b6364}
.dot.grey-hollow{background:transparent;border:2px solid #6b6364}

/* footer */
.site-footer{position:absolute;left:0;top:2452px;width:1200px;height:321px;background:var(--footer);color:var(--white)}
.footer-col{position:absolute;top:42px}
.footer-col h4{font-family:"Montserrat",sans-serif;font-weight:600;font-size:16.5px;letter-spacing:.5px;margin-bottom:16px}
.footer-col li{list-style:none;font-size:13.5px;line-height:30px;color:#eef4fb}
.footer-col .contact-line{display:flex;align-items:center;gap:12px}
.footer-divider{position:absolute;top:40px;width:1px;height:190px;background:rgba(255,255,255,.18)}
.social{display:flex;gap:5px;margin-top:14px}
.social span{width:36px;height:36px;border-radius:50%;border:2px solid var(--white);background:rgba(255,255,255,.15)}
.footer-rule{position:absolute;left:100px;top:250px;width:1000px;height:1px;background:rgba(255,255,255,.5)}
.copyright{position:absolute;left:100px;top:273px;font-size:12px;color:#e8f0fa}
</style>
</head>
<body>

<header class="site-header">
  <div class="brand">
    <div class="brand-mark"></div>
    <div class="brand-name">VANTAGE<br>INTERIORS</div>
  </div>
  <nav class="main-nav">
    <a class="active" style="left:537px">HOME</a>
    <a style="left:632px">SERVICES</a>
    <a style="left:755px">PRODUCTS</a>
    <a style="left:887px">GALLERY</a>
    <a style="left:1007px">CONTACT US</a>
  </nav>
  <div class="nav-underline"></div>
</header>

<section class="hero" role="img" aria-label="Modern open-plan kitchen and dining room with pendant lights">
  <h1 class="hero-title">VANTAGE INTERIORS</h1>
  <div class="dots" style="left:563px;top:515px">
    <span class="dot hollow"></span><span class="dot"></span><span class="dot"></span><span class="dot"></span>
  </div>
  <svg class="hero-curve" width="1200" height="601" viewBox="0 0 1200 601"><path d="M0 601 Q600 545 1200 601 Z" fill="#fff"/></svg>
</section>

<section class="welcome">
  <h2 class="section-title abs center" style="top:742px">WELCOME TO <span class="accent">VANTAGE INTERIORS</span></h2>
  <p class="lead abs" style="left:170px;top:800px;width:860px;text-align:center">Sed ut perspiciatis unde omnis iste natus error sit voluptatem accusantium doloremque laudantium, totam rem aperiam, eaque ipsa quae ab illo inventore veritatis et quasi architecto beatae vitae dicta sunt explicabo. Nemo enim ipsam voluptatem quia voluptas sit aspernatur aut odit aut fugit, sed quia conseqSed ut perspiciatis unde omnis iste natus error sit voluptate</p>

  <div class="market-card" style="left:170px">
    <svg width="72" height="56" viewBox="0 0 72 56" aria-hidden="true">
      <path d="M4 28 L36 4 L68 28 L62 28 L36 9 L10 28 Z" fill="#6d6f78"/>
      <rect x="52" y="6" width="7" height="14" fill="#6d6f78"/>
      <path d="M12 28 L36 11 L60 28 L60 52 L12 52 Z" fill="#6d6f78"/>
      <rect x="20" y="34" width="10" height="18" fill="#fff"/>
      <rect x="38" y="34" width="14" height="10" fill="#fff"/>
    </svg>
    <h3>RESIDENTIAL MARKETS</h3>
    <p>Sed ut perspiciatis unde omnis iste natus error sit volu ptatem accusantium ntium, totam rem aperiam, eaqu</p>
  </div>

  <div class="market-card" style="left:658px">
    <svg width="72" height="66" viewBox="0 0 72 66" aria-hidden="true" style="top:62px">
      <rect x="20" y="4" width="30" height="60" fill="#6d6f78"/>
      <rect x="4" y="24" width="16" height="40" fill="#6d6f78"/>
      <rect x="50" y="20" width="16" height="44" fill="#6d6f78"/>
      <g fill="#fff">
        <rect x="25" y="10" width="6" height="6"/><rect x="39" y="10" width="6" height="6"/>
        <rect x="25" y="22" width="6" height="6"/><rect x="39" y="22" width="6" height="6"/>
        <rect x="25" y="34" width="6" height="6"/><rect x="39" y="34" width="6" height="6"/>
        <rect x="8" y="30" width="6" height="5"/><rect x="8" y="42" width="6" height="5"/>
        <rect x="55" y="28" width="6" height="5"/><rect x="55" y="40" width="6" height="5"/>
        <rect x="30" y="50" width="10" height="14"/>
      </g>
    </svg>
    <h3>COMMERCIAL MARKETS</h3>
    <p>Sed ut perspiciatis unde omnis iste natus error sit volu ptatem accusantium ntium, totam rem aperiam, eaqu</p>
  </div>
</section>

<section class="specialise" role="img" aria-label="Blue-toned sofa in a living room">
  <h2>We Specialise in Interior Decoration to<br>Residential and Commercial Markets</h2>
  <p>Ut enim ad minim veniam, quis nostrud exercitation ullamco laboris nisi ut aliquip ex ea commodo consequat. Duis aute irure dolor in reprehenderit in voluptate velit esse cillum dolore eu fugiat nulla pariatur. Excepteur sint occaecat cupidatat non proident, sunt in culpa qui officia deserunt mollit anim id est laborum</p>
  <div class="btn-outline">VIEW MORE</div>
</section>

<section class="services">
  <h2 class="section-title abs center" style="top:1646px">OUR SERVICES <span class="accent">WE PROVIDE</span></h2>
  <p class="lead abs center" style="top:1703px;font-size:13.5px;color:#777">Quis autem vel eum iure reprehenderit qui in ea voluptate velit esse quam nihil molestiae</p>

  <div class="service-card" style="left:98px">
    <div class="service-photo" role="img" aria-label="Office interior with wood panelled wall" style="background:linear-gradient(90deg,#5b7f8a 0%,#7a4a2c 35%,#8a5633 65%,#c8c6c2 100%)"></div>
    <h3>OFFICE DECORATION</h3>
  </div>
  <div class="service-card" style="left:444px">
    <div class="service-photo" role="img" aria-label="Living room with white sofa and burgundy feature wall" style="background:linear-gradient(180deg,#6e2f3d 0%,#8a4656 55%,#d9ccc4 80%,#c3b7ae 100%)"></div>
    <h3>HOME DECORATION</h3>
  </div>
  <div class="service-card" style="left:790px">
    <div class="service-photo" role="img" aria-label="Hallway with stone-textured feature wall" style="background:linear-gradient(90deg,#2a2a28 0%,#9c9a92 30%,#b8b5ac 60%,#8d8b82 85%,#3a3a38 100%)"></div>
    <h3>FEATURE WALLS</h3>
  </div>
</section>

<section class="testimonials" role="img" aria-label="Faded coastal city skyline at dusk">
  <h2 class="section-title abs center" style="top:46px;font-size:30px">WHAT CLIENTS SAY</h2>
  <span class="quote-mark" style="left:150px;top:100px">&ldquo;</span>
  <p class="quote-text">La dermocosmesi si occupa attraverso l'utilizzo di prodotti tecnologicamente innovativi e sostanze polifunzionali di garantire e mantenere lo stato di salute, di benessere e quindi di bellezza della pelle. Fin dall'antichità sia l'uomo che la donna si sono occupati ampiamente del proprio aspetto fisico impiegando tempo e risorse, indipendentemente dal ceto sociale</p>
  <span class="quote-mark" style="left:996px;top:150px">&rdquo;</span>
  <p class="quote-author"><span class="name">- Daniel Reyes,</span> Businessman</p>
  <div class="dots" style="left:563px;top:280px">
    <span class="dot grey-hollow"></span><span class="dot grey"></span><span class="dot grey"></span><span class="dot grey"></span>
  </div>
</section>

<footer class="site-footer">
  <div class="footer-col" style="left:100px">
    <h4>COMPANY</h4>
    <ul><li>Home</li><li>Services</li><li>Products</li><li>Gallery</li><li>Contact us</li></ul>
  </div>
  <div class="footer-divider" style="left:233px"></div>
  <div class="footer-col" style="left:275px">
    <h4>SERVICES</h4>
    <ul><li>Office Decoration</li><li>Home Decoration</li><li>Features Walls</li><li>Other Services</li></ul>
  </div>
  <div class="footer-divider" style="left:457px"></div>
  <div class="footer-col" style="left:497px">
    <h4>GET IN TOUCH</h4>
    <ul>
      <li class="contact-line"><svg width="14" height="14" viewBox="0 0 24 24" aria-hidden="true"><path fill="#fff" d="M6.6 10.8a15.1 15.1 0 0 0 6.6 6.6l2.2-2.2a1 1 0 0 1 1-.25 11.4 11.4 0 0 0 3.6.57 1 1 0 0 1 1 1V20a1 1 0 0 1-1 1A17 17 0 0 1 3 4a1 1 0 0 1 1-1h3.5a1 1 0 0 1 1 1c0 1.25.2 2.45.57 3.57a1 1 0 0 1-.25 1z"/></svg>Call us on (01) 48201937</li>
      <li class="contact-line"><svg width="14" height="12" viewBox="0 0 24 18" aria-hidden="true"><path fill="#fff" d="M0 0h24v2L12 10 0 2z M0 4l12 8 12-8v14H0z"/></svg>hello@vantagemail.com</li>
    </ul>
  </div>
  <div class="footer-divider" style="left:730px"></div>
  <div class="footer-col" style="left:769px">
    <h4>WHY US</h4>
    <ul><li>Customers</li><li>Team</li><li>FAQ</li><li>Contact</li></ul>
  </div>
  <div class="footer-divider" style="left:886px"></div>
  <div class="footer-col" style="left:925px">
    <h4>FOLLLOW US</h4>
    <ul><li>Please connect with us on</li></ul>
    <div class="social"><span></span><span></span><span></span><span></span></div>
  </div>
  <div class="footer-rule"></div>
  <p class="copyright">© 2016 Company Name &nbsp;All right reserved &nbsp;Term of Use</p>
</footer>

</body>
</html>
```